Modify ShopVantor HomePage Template

The scope of the project is to take the current template for our ShopVantor Website and make several modifications. The goal is to model the current HOME template to mirror the Quillon.com homepage
Designer MUST be familiar with Tessel CLI Framework. Below is a list of tasks we need done, along with the Template Files, Sample Images and some additional information about the templates. Final images will be sent after we select the winner.
Task 1 - Modify Homepage Carousel so that the images do not look distorted and fit the page well - The current image is way to big and takes away from the feel of the page (please visit www.greenmapleusa.com and use the the preview code "q8tkrwz5hd") ALSO - Please see the www.Quillon.com homepage for the size of images we want the Carousel to reflect.
Please ensure the carousel image will retain the same dimensions as the one on Quillons.com homepage (FYI - Tessel themes typically use carousel dimensions between 1200 x 600 pixels and 1600 x 900 pixels. Images outside these ranges can run the risk of becoming distorted since the theme will stretch or squish an image to make it fit. Since all Tessel themes are responsive, the carousel will adjust itself to suit the screen size.)
Task 3 - Adding a "More from GreenMaple" Section below the Featured Products section
Task 4 - Adding a placeholder for 2 images in the "More from GreenMaple" Section similar to Quillons.com - The two images need to be have a clickable URL and will direct the shopper to two pages of our choosing.
RIGHT Image Placeholder - Image of the Assorted Fabric Bandage. Content Heading "Assorted Bandages" Line 2 "The perfect way to promote healing" Line 3 "Shop Now" with link to http://greenmapleusa.com/bandages/
LEFT Image Placeholder - Comet_Grp Image. Content Heading "Want to save even more at Orbit?" Line 2 "Pre-order now and watch your savings take off" Line 3 "Pre-Order" with link to http://greenmapleusa.com/gloves/
Task 5 - Return the Entire Template with the changes page and note specifically which files were altered
Task 6 - Provide support for 30 days after the modified template is uploaded - You are responsible to provide support ONLY pertaining to ensuring YOUR changes work well with the site without any problems.
Harbor Pale Template ZIP (Version: 1.12.0 Developed and supported by Mosaic Guild)
Additional Details
Visit www.Quillons.com
Coding
Coded - Design and coding required
Number of Pages Required
1 page
Font styles to use
Other font styles liked:
- Use fonts provided in Template
Look and feel
Each slider illustrates characteristics of the customer's brand and the style your logo design should communicate.

```html
<!DOCTYPE html>
<html lang="en">
<head>
<meta charset="utf-8">
<title>GreenMaple — Home</title>
<link href="https://fonts.googleapis.com/css2?family=Jost:wght@400;500;600&display=swap" rel="stylesheet">
<style>
  :root {
    --canvas: #efefef;
    --white: #ffffff;
    --utility: #f4f4f4;
    --hero: #f2f2f2;
    --navy: #2f4a78;
    --ink: #333a44;
    --muted: #7c8088;
    --brand-blue: #2b6cb8;
    --button-blue: #1c9be0;
    --card-blue: #eef5fa;
    --teal: #6ccbd6;
    --teal-deep: #1f5f6a;
    --stone: #e2e2e2;
    --section-grey: #f7f7f7;
    --tile-grey: #e4e4e4;
    --footer: #8a8d91;
    --footer-text: #f4f5f6;
    --black: #222426;
  }
  * { box-sizing: border-box; margin: 0; padding: 0; }
  html, body { width: 1200px; height: 2899px; overflow: hidden; }
  body { background: var(--canvas); font-family: "Jost", Arial, sans-serif; color: var(--ink); }
  .page { position: absolute; left: 46px; top: 60px; width: 1109px; height: 2779px; background: var(--white); overflow: hidden; }
  .abs { position: absolute; }

  .utility-bar { left: 0; top: 0; width: 1109px; height: 39px; background: var(--utility); }
  .utility-links { right: 174px; top: 0; height: 39px; display: flex; align-items: center; gap: 20px; font-size: 10px; color: var(--ink); }
  .utility-links span { display: flex; align-items: center; gap: 5px; }

  .site-header { left: 0; top: 39px; width: 1109px; height: 98px; }
  .logo { left: 172px; top: 32px; display: flex; align-items: center; gap: 8px; font-size: 28px; font-weight: 500; color: var(--brand-blue); letter-spacing: -0.3px; }
  .logo-dot { width: 22px; height: 22px; border-radius: 50%; background: var(--brand-blue); }
  .main-nav { right: 174px; top: 49px; display: flex; gap: 22px; font-size: 11px; text-transform: uppercase; color: var(--ink); letter-spacing: 0.3px; }
  .main-nav span { display: flex; align-items: center; gap: 4px; }

  .hero { left: 0; top: 137px; width: 1109px; height: 397px; background: var(--hero); }
  .hero-title { left: 172px; top: 116px; font-size: 25px; line-height: 33px; font-weight: 400; color: var(--ink); }
  .hero-text { left: 172px; top: 196px; width: 330px; font-size: 12.5px; line-height: 17px; color: var(--ink); }
  .hero-button { left: 172px; top: 250px; width: 106px; height: 35px; background: var(--button-blue); color: var(--white); font-size: 9px; font-weight: 600; letter-spacing: 1px; display: flex; align-items: center; justify-content: center; }
  .hero-visual { left: 670px; top: 0; width: 439px; height: 397px; background: radial-gradient(ellipse at 60% 45%, #7fc4ee 0%, #a9d6f2 35%, #f2f2f2 72%); }
  .hero-dots { left: 540px; top: 365px; display: flex; gap: 6px; }
  .hero-dots i { width: 5px; height: 5px; border-radius: 50%; background: #c3c3c3; display: block; }

  .section-title { width: 1109px; text-align: center; color: var(--navy); }
  .featured-title { top: 624px; font-size: 16px; }
  .featured-sub { top: 652px; font-size: 11px; color: var(--ink); }

  .product-card { background: var(--card-blue); }
  .product-shot { position: absolute; left: 12%; top: 14%; width: 76%; height: 72%; border-radius: 4px; }
  .shot-bandage { background: linear-gradient(135deg, #dfe9f4, #2e6fb8 55%, #d9a07a); }
  .shot-nitrile { background: linear-gradient(135deg, #ffffff, #e3ecf4 60%, #f0b85c); }
  .shot-blue { background: linear-gradient(135deg, #ffffff 30%, #3b7fd0); }
  .shot-red { background: linear-gradient(135deg, #ffffff 30%, #c8282e); }
  .shot-pink { background: linear-gradient(135deg, #ffffff 30%, #d83c8c); }
  .product-name { text-align: center; font-size: 12.5px; font-weight: 500; color: var(--ink); }
  .product-detail { text-align: center; font-size: 9.5px; color: var(--ink); }

  .promo-orbit { left: 172px; top: 1558px; width: 373px; height: 292px; background: var(--teal); }
  .promo-bandages { left: 561px; top: 1558px; width: 373px; height: 292px; background: var(--stone); }
  .promo-heading { font-size: 19px; line-height: 25px; color: var(--ink); }
  .promo-line { font-size: 15.5px; line-height: 24px; color: var(--teal-deep); }
  .promo-bandages .promo-line { color: var(--ink); }
  .promo-link { font-size: 9px; font-weight: 600; letter-spacing: 1.6px; color: var(--ink); text-transform: uppercase; border-bottom: 1px solid var(--ink); padding-bottom: 2px; }
  .rocket-art { left: 0; top: 110px; width: 373px; height: 182px; background: linear-gradient(180deg, rgba(108,203,214,0) 0%, #5db7b9 70%, #3c8f8d 100%); }
  .bandage-art { left: 148px; top: 110px; width: 225px; height: 182px; background: linear-gradient(135deg, #f4f6f8 20%, #2e6fb8 60%, #d9a07a); }

  .more-section { left: 0; top: 1945px; width: 1109px; height: 650px; background: var(--section-grey); }
  .more-title { top: 2036px; font-size: 20px; letter-spacing: 3px; font-weight: 500; }
  .more-sub { top: 2075px; font-size: 8px; letter-spacing: 1.6px; color: var(--muted); text-transform: uppercase; }
  .more-tile { width: 240px; height: 232px; background: var(--tile-grey); display: flex; align-items: center; justify-content: center; }
  .more-heading { width: 240px; text-align: center; font-size: 12px; font-weight: 500; letter-spacing: 2px; color: var(--navy); text-transform: uppercase; }
  .more-text { width: 240px; text-align: center; font-size: 10px; line-height: 17px; color: var(--muted); }

  .site-footer { left: 0; top: 2595px; width: 1109px; height: 184px; background: var(--footer); color: var(--footer-text); }
  .footer-col { top: 60px; font-size: 9.5px; line-height: 13.5px; }
  .footer-col h4 { font-size: 9.5px; font-weight: 600; margin-bottom: 2px; }
  .newsletter-label { left: 688px; top: 60px; font-size: 9.5px; font-weight: 600; }
  .newsletter-input { left: 688px; top: 81px; width: 180px; height: 33px; background: var(--white); color: #a0a3a8; font-size: 9.5px; padding-left: 10px; display: flex; align-items: center; }
  .newsletter-submit { left: 873px; top: 81px; width: 61px; height: 33px; background: var(--black); color: var(--white); font-size: 9px; font-weight: 600; letter-spacing: 1px; display: flex; align-items: center; justify-content: center; }
  .payment-row { left: 688px; top: 126px; display: flex; gap: 12px; }
  .payment-mark { width: 36px; height: 18px; border-radius: 3px; background: #b4b7bb; }
</style>
</head>
<body>
<div class="page">

  <div class="abs utility-bar"></div>
  <div class="abs utility-links">
    <span><svg width="10" height="10" viewBox="0 0 10 10"><circle cx="4" cy="4" r="3" fill="none" stroke="#555" stroke-width="1.2"/><line x1="6.2" y1="6.2" x2="9.2" y2="9.2" stroke="#555" stroke-width="1.2"/></svg>Search</span>
    <span><svg width="11" height="10" viewBox="0 0 11 10"><path d="M0.5 1h2l1.5 5.5h5l1.3-4H3" fill="none" stroke="#555" stroke-width="1.1"/><circle cx="4.5" cy="8.6" r="0.9" fill="#555"/><circle cx="8.3" cy="8.6" r="0.9" fill="#555"/></svg>Cart</span>
    <span><svg width="9" height="10" viewBox="0 0 9 10"><circle cx="4.5" cy="2.7" r="2.2" fill="#555"/><path d="M0.3 10c0-3 1.9-4.6 4.2-4.6S8.7 7 8.7 10z" fill="#555"/></svg>Sign in</span>
  </div>

  <header class="abs site-header">
    <div class="abs logo"><span class="logo-dot"></span>GreenMaple</div>
    <nav class="abs main-nav">
      <span>Home</span>
      <span>Gloves <svg width="7" height="5" viewBox="0 0 7 5"><path d="M0.5 0.8L3.5 3.8 6.5 0.8" fill="none" stroke="#555"/></svg></span>
      <span>Wound Care <svg width="7" height="5" viewBox="0 0 7 5"><path d="M0.5 0.8L3.5 3.8 6.5 0.8" fill="none" stroke="#555"/></svg></span>
      <span>Shipping &amp; Returns</span>
      <span>Contact</span>
    </nav>
  </header>

  <section class="abs hero">
    <div class="abs hero-visual" role="img" aria-label="Photo of hands pulling on blue nitrile gloves"></div>
    <h1 class="abs hero-title">Building a culture of Care,<br>Giving and growth</h1>
    <p class="abs hero-text">Lorem ipsum dolor sit amet, consectetur adipiscing elit, sed do eiusmod tempor incididunt ut labore</p>
    <div class="abs hero-button">GO TO STORE</div>
    <div class="abs hero-dots"><i></i><i></i><i></i></div>
  </section>

  <h2 class="abs section-title featured-title">Featured Products</h2>
  <p class="abs section-title featured-sub">All designed and formulated for a quality shave.</p>

  <div class="abs product-card" style="left:172px;top:735px;width:373px;height:284px;"><div class="product-shot shot-bandage" role="img" aria-label="Box of flexible fabric adhesive bandages"></div></div>
  <div class="abs product-card" style="left:561px;top:735px;width:373px;height:284px;"><div class="product-shot shot-nitrile" role="img" aria-label="Box of large nitrile medical gloves"></div></div>
  <p class="abs product-name" style="left:172px;top:1037px;width:373px;">Waterproof Adhesive Bandages</p>
  <p class="abs product-detail" style="left:172px;top:1059px;width:373px;">Assorted, Elastic and Flexible Fabric</p>
  <p class="abs product-name" style="left:561px;top:1037px;width:373px;">Large Nitrile Medical Gloves</p>
  <p class="abs product-detail" style="left:561px;top:1059px;width:373px;">Cuffed and Powder-Free</p>

  <div class="abs product-card" style="left:172px;top:1161px;width:230px;height:228px;"><div class="product-shot shot-blue" role="img" aria-label="Box of sterile latex surgical gloves, blue pack"></div></div>
  <div class="abs product-card" style="left:435px;top:1161px;width:230px;height:228px;"><div class="product-shot shot-red" role="img" aria-label="Box of sterile latex surgical gloves, red pack"></div></div>
  <div class="abs product-card" style="left:704px;top:1161px;width:230px;height:228px;"><div class="product-shot shot-pink" role="img" aria-label="Box of sterile latex surgical gloves, pink pack"></div></div>
  <p class="abs product-name" style="left:172px;top:1403px;width:230px;">7.0 Sterile Latex Surgical Gloves</p>
  <p class="abs product-detail" style="left:172px;top:1425px;width:230px;">Cuffed and Powder-Free</p>
  <p class="abs product-name" style="left:435px;top:1403px;width:230px;">7.0 Sterile Latex Surgical Gloves</p>
  <p class="abs product-detail" style="left:435px;top:1425px;width:230px;">Cuffed and Powder-Free</p>
  <p class="abs product-name" style="left:704px;top:1403px;width:230px;">7.0 Sterile Latex Surgical Gloves</p>
  <p class="abs product-detail" style="left:704px;top:1425px;width:230px;">Cuffed and Powder-Free</p>

  <div class="abs promo-orbit">
    <div class="abs rocket-art" role="img" aria-label="Illustration of a rocket lifting off among hot air balloons"></div>
    <p class="abs promo-heading" style="left:54px;top:55px;">Want to save even<br>more at Orbit?</p>
    <p class="abs promo-line" style="left:54px;top:107px;">Pre-order now and watch<br>your savings take off</p>
    <span class="abs promo-link" style="left:54px;top:177px;">Pre-Order</span>
  </div>

  <div class="abs promo-bandages">
    <div class="abs bandage-art" role="img" aria-label="Box of assorted fabric bandages"></div>
    <p class="abs promo-heading" style="left:64px;top:55px;">Assorted Bandages</p>
    <p class="abs promo-line" style="left:64px;top:87px;">The perfect way to<br>promote healing</p>
    <span class="abs promo-link" style="left:64px;top:145px;">Shop Now</span>
  </div>

  <section class="abs more-section"></section>
  <h2 class="abs section-title more-title">MORE FROM GREENMAPLE</h2>
  <p class="abs section-title more-sub">We do more than make bandages, you know.</p>

  <div class="abs more-tile" style="left:172px;top:2167px;"><svg width="92" height="80" viewBox="0 0 92 80"><rect x="14" y="0" width="78" height="64" rx="6" fill="#fff"/><rect x="0" y="14" width="76" height="66" rx="6" fill="#fff" stroke="#e4e4e4" stroke-width="4"/><circle cx="52" cy="38" r="6" fill="#e4e4e4"/><path d="M10 70l18-20 14 14 8-8 18 14z" fill="#e4e4e4"/></svg></div>
  <div class="abs more-tile" style="left:433px;top:2167px;"><svg width="92" height="80" viewBox="0 0 92 80"><rect x="14" y="0" width="78" height="64" rx="6" fill="#fff"/><rect x="0" y="14" width="76" height="66" rx="6" fill="#fff" stroke="#e4e4e4" stroke-width="4"/><circle cx="52" cy="38" r="6" fill="#e4e4e4"/><path d="M10 70l18-20 14 14 8-8 18 14z" fill="#e4e4e4"/></svg></div>
  <div class="abs more-tile" style="left:693px;top:2167px;"><svg width="92" height="80" viewBox="0 0 92 80"><rect x="14" y="0" width="78" height="64" rx="6" fill="#fff"/><rect x="0" y="14" width="76" height="66" rx="6" fill="#fff" stroke="#e4e4e4" stroke-width="4"/><circle cx="52" cy="38" r="6" fill="#e4e4e4"/><path d="M10 70l18-20 14 14 8-8 18 14z" fill="#e4e4e4"/></svg></div>

  <h3 class="abs more-heading" style="left:172px;top:2426px;">Affiliates Programs</h3>
  <p class="abs more-text" style="left:172px;top:2450px;">Neque porro quisquam est qui dolorem ipsum quia dolor sit amet, consectetur.</p>
  <h3 class="abs more-heading" style="left:433px;top:2426px;">From the Blog</h3>
  <p class="abs more-text" style="left:433px;top:2450px;">Neque porro quisquam est qui dolorem ipsum quia dolor sit amet, consectetur.</p>
  <h3 class="abs more-heading" style="left:693px;top:2426px;">Shipping &amp; Returns</h3>
  <p class="abs more-text" style="left:693px;top:2450px;">Neque porro quisquam est qui dolorem ipsum quia dolor sit amet, consectetur.</p>

  <footer class="abs site-footer">
    <div class="abs footer-col" style="left:180px;"><h4>Shop</h4>Gloves<br>Wound Care<br>Shipping &amp; Returns</div>
    <div class="abs footer-col" style="left:354px;"><h4>Account</h4>Sign up<br>Gift Certificates<br>Support<br>FAQs</div>
    <div class="abs footer-col" style="left:481px;"><h4>Company</h4>About<br>Legal<br>Contact</div>
    <p class="abs newsletter-label">Subscribe to our newsletter</p>
    <div class="abs newsletter-input">Enter your email address</div>
    <div class="abs newsletter-submit">SUBMIT</div>
    <div class="abs payment-row"><span class="payment-mark"></span><span class="payment-mark"></span><span class="payment-mark"></span><span class="payment-mark"></span><span class="payment-mark"></span></div>
  </footer>

</div>
</body>
</html>
```